Brennock Holdings LLC, new Business cards

I'm moving offices and need new cards. Plus I'm open to modifying the current design of my card. I will keep the logo but would like to explore other layouts and fonts for the design. I've included the current double sided card for reference. I Like the navy color and white. Might be open to grays or silver. Needs to be clean and elegant.

Target Market(s)

Investors, buyers & sellers of private equities and real estate.

Contact Information for Business Card

Brennock Holdings
Desmond K.R. Whitfield, Managing Principal
418 Harwick Ave., Suite 310
Denver, CO 80299
M: 970-555-0147, O: 303-555-0193
Desmond@brennockholdings.example
Brennockholdings.example

Colors
0354a2
ffffff
c4c4c4

Requirements
Must have
• Business card details.
• Logo raised or embossed, it was designed after a wax seal. Current has raised ink.
Nice to have
• Space on card to write additional notes.

```html
<!DOCTYPE html>
<html lang="en">
<head>
<meta charset="utf-8">
<title>Brennock Holdings – Business Cards</title>
<link rel="stylesheet" href="https://fonts.googleapis.com/css2?family=Lato:wght@400;700&display=swap">
<style>
  :root{
    --navy:#23205e;
    --white:#ffffff;
    --silver:#c2c2c2;
    --silver-line:#c8c8c8;
    --ink:#1c1c2a;
    --stage:#3b3b3d;
  }
  *{margin:0;padding:0;box-sizing:border-box}
  html,body{width:1200px;height:900px;overflow:hidden;background:var(--stage)}
  body{position:relative;font-family:"Lato",sans-serif}
  .card{position:absolute;width:540px;height:310px;border-radius:18px;overflow:hidden}
  .card--back{left:80px;top:80px;background:var(--silver)}
  .card--front{left:580px;top:500px;background:var(--white)}

  .brand-mark{position:absolute;display:flex;align-items:center;gap:10px;color:var(--navy);font-weight:700}
  .brand-mark__dot{border-radius:50%;background:var(--navy);flex:none}
  .card--back .brand-mark{left:50%;top:112px;transform:translateX(-50%);font-size:26px;white-space:nowrap}
  .card--back .brand-mark__dot{width:30px;height:30px}
  .back-url{position:absolute;left:0;right:0;top:220px;text-align:center;color:var(--navy);font-size:13px;letter-spacing:2px}

  .card--front .brand-mark{right:30px;top:52px;font-size:17px;white-space:nowrap}
  .card--front .brand-mark__dot{width:20px;height:20px}

  .swoosh{position:absolute;left:0;top:0;width:540px;height:310px}

  .holder{position:absolute;left:44px;top:84px}
  .holder__name{color:var(--navy);font-size:28px;font-weight:700;line-height:1}
  .holder__title{color:var(--navy);font-size:14px;margin-top:4px}
  .holder__rule{width:62px;height:2px;background:var(--navy);margin-top:9px}

  .contacts{position:absolute;left:44px;top:148px;list-style:none}
  .contacts li{display:flex;align-items:center;gap:8px;color:var(--ink);font-size:13.5px;line-height:19px}
  .contacts svg{width:13px;height:13px;flex:none}

  .address{position:absolute;left:44px;top:270px;color:var(--white);font-size:13px;line-height:17px}
</style>
</head>
<body>

<section class="card card--back" aria-label="Card back">
  <div class="brand-mark"><span class="brand-mark__dot"></span>Brennock Holdings</div>
  <p class="back-url">www.brennockholdings.example</p>
</section>

<section class="card card--front" aria-label="Card front">
  <svg class="swoosh" viewBox="0 0 540 310" aria-hidden="true">
    <path d="M540 95 C505 170 440 200 360 214" fill="none" stroke="var(--silver-line)" stroke-width="6"/>
    <path d="M0 310 L0 262 C80 250 220 242 340 230 C450 218 520 182 540 120 L540 310 Z" fill="var(--navy)"/>
  </svg>

  <div class="brand-mark"><span class="brand-mark__dot"></span>Brennock Holdings</div>

  <div class="holder">
    <h1 class="holder__name">Desmond K.R. Whitfield</h1>
    <p class="holder__title">Managing Principal</p>
    <div class="holder__rule"></div>
  </div>

  <ul class="contacts">
    <li><svg viewBox="0 0 12 12"><polygon points="6,0 11.2,3 11.2,9 6,12 0.8,9 0.8,3" fill="var(--navy)"/><rect x="4.3" y="3" width="3.4" height="6" rx="0.6" fill="none" stroke="#fff" stroke-width="0.9"/></svg>970-555-0147</li>
    <li><svg viewBox="0 0 12 12"><polygon points="6,0 11.2,3 11.2,9 6,12 0.8,9 0.8,3" fill="var(--navy)"/><path d="M4 3.5 L5 5 L4.6 5.6 Q5.4 6.9 6.4 7.4 L7 7 L8.5 8 L7.8 8.8 Q4.6 8 3.3 4.4 Z" fill="#fff"/></svg>720-555-0162</li>
    <li><svg viewBox="0 0 12 12"><polygon points="6,0 11.2,3 11.2,9 6,12 0.8,9 0.8,3" fill="var(--navy)"/><rect x="3.2" y="4" width="5.6" height="4" fill="none" stroke="#fff" stroke-width="0.8"/><path d="M3.2 4 L6 6.2 L8.8 4" fill="none" stroke="#fff" stroke-width="0.8"/></svg>info@brennockholdings.example</li>
    <li><svg viewBox="0 0 12 12"><polygon points="6,0 11.2,3 11.2,9 6,12 0.8,9 0.8,3" fill="var(--navy)"/><circle cx="6" cy="6" r="2.7" fill="none" stroke="#fff" stroke-width="0.8"/><path d="M3.3 6 H8.7 M6 3.3 V8.7" stroke="#fff" stroke-width="0.6"/></svg>www.brennockholdings.example</li>
  </ul>

  <p class="address">418 Harwick Ave.<br>Suite 310, Denver, CO 80299</p>
</section>

</body>
</html>
```